Fernwood Chiropractic
letterhead/business cards
Project: Fernwood Chiropractic
Fernwood Chiropractic - Health
Creative Brief
Professional
Dr. Gavin P. Holcombe
Chiropractor
4817 Dunmore Road Building 2, Suite C-21 Philadelphia, PA 19144
drholcombe@fernwoodchiro-example.com
www.fernwoodchiro-example.com

```html
<!DOCTYPE html>
<html lang="en">
<head>
<meta charset="utf-8">
<title>Fernwood Chiropractic – Business Card</title>
<link href="https://fonts.googleapis.com/css2?family=Cinzel:wght@500;600&family=Cormorant+Garamond:wght@500;600&display=swap" rel="stylesheet">
<style>
  :root {
    --page-bg: #e9ebee;
    --card-bg: #f7f8f9;
    --brand-blue: #2a6fa8;
    --green-light: #5cc23f;
    --green-mid: #39a52a;
    --green-dark: #238a1e;
    --silver-light: #f4f5f6;
    --silver-mid: #b9bdc1;
    --silver-dark: #8d9296;
    --pointer: #1f5f1c;
    --white: #ffffff;
  }
  * { margin: 0; padding: 0; box-sizing: border-box; }
  html, body { width: 1200px; height: 768px; overflow: hidden; }
  body {
    background: var(--page-bg);
    font-family: "Cormorant Garamond", Georgia, serif;
    position: relative;
  }
  .business-card {
    position: absolute;
    left: 100px; top: 98px;
    width: 1000px; height: 572px;
    background: var(--card-bg);
    box-shadow: 0 14px 40px rgba(0,0,0,0.18);
    overflow: hidden;
  }
  .brand {
    position: absolute;
    left: 0; right: 0; top: 118px;
    display: flex; align-items: center; justify-content: center; gap: 22px;
  }
  .brand-mark {
    width: 64px; height: 64px; border-radius: 50%;
    background: var(--green-mid);
  }
  .brand-name {
    font-family: "Cinzel", Georgia, serif;
    font-weight: 600;
    color: var(--brand-blue);
    font-size: 44px;
    line-height: 1.05;
    letter-spacing: 1px;
  }
  .contact-band {
    position: absolute;
    left: 0; right: 0; top: 328px; height: 168px;
    background: linear-gradient(180deg, var(--green-light) 0%, var(--green-mid) 55%, var(--green-dark) 100%);
  }
  .silver-rule {
    position: absolute; left: 0; right: 0; height: 12px;
    background: linear-gradient(180deg, var(--silver-light) 0%, var(--silver-mid) 50%, var(--silver-dark) 100%);
  }
  .silver-rule.top { top: 316px; }
  .silver-rule.bottom { top: 496px; }
  .band-pointer {
    position: absolute; left: 218px; top: 304px;
    width: 0; height: 0;
    border-left: 18px solid transparent;
    border-right: 18px solid transparent;
    border-top: 22px solid var(--pointer);
    z-index: 2;
  }
  .identity {
    position: absolute; left: 150px; top: 362px;
    color: var(--white); text-align: center; width: 260px;
  }
  .identity .name {
    font-family: "Cinzel", Georgia, serif; font-weight: 500;
    font-size: 22px; letter-spacing: 1px;
  }
  .identity .title {
    font-family: "Cinzel", Georgia, serif; font-weight: 500;
    font-size: 17px; letter-spacing: 1px; margin-top: 2px;
  }
  .band-divider {
    position: absolute; left: 468px; top: 348px;
    width: 1px; height: 128px; background: rgba(255,255,255,0.75);
  }
  .contact-list {
    position: absolute; left: 494px; top: 344px;
    list-style: none; color: var(--white);
    font-size: 16px; font-weight: 600; line-height: 1.2;
  }
  .contact-list li { display: flex; align-items: center; gap: 10px; margin-bottom: 6px; }
  .contact-list li.address { align-items: flex-start; margin-bottom: 10px; }
  .contact-list svg { width: 16px; height: 16px; flex: none; }
</style>
</head>
<body>
  <div class="business-card">
    <div class="brand">
      <div class="brand-mark"></div>
      <div class="brand-name">Fernwood<br>Chiropractic</div>
    </div>

    <div class="silver-rule top"></div>
    <div class="band-pointer"></div>
    <div class="contact-band"></div>
    <div class="silver-rule bottom"></div>

    <div class="identity">
      <div class="name">Dr. Gavin P. Holcombe</div>
      <div class="title">Chiropractor</div>
    </div>

    <div class="band-divider"></div>

    <ul class="contact-list">
      <li class="address">
        <svg viewBox="0 0 16 16"><path d="M8 1a5 5 0 0 0-5 5c0 4 5 9 5 9s5-5 5-9a5 5 0 0 0-5-5zm0 7a2 2 0 1 1 0-4 2 2 0 0 1 0 4z" fill="#fff"/></svg>
        <span>4817 Dunmore Road, Building 2<br>Suite C-21 Philadelphia, PA 19144</span>
      </li>
      <li>
        <svg viewBox="0 0 16 16"><path d="M4 1.5l2.5 3-1.5 1.5c.8 1.8 2.2 3.2 4 4l1.5-1.5 3 2.5-1.5 2.5C7 13.5 2.5 9 2 3z" fill="#fff"/></svg>
        <span>(215) 555-0148</span>
      </li>
      <li>
        <svg viewBox="0 0 16 16"><path d="M4 1.5l2.5 3-1.5 1.5c.8 1.8 2.2 3.2 4 4l1.5-1.5 3 2.5-1.5 2.5C7 13.5 2.5 9 2 3z" fill="#fff"/></svg>
        <span>(215) 555-0172</span>
      </li>
      <li>
        <svg viewBox="0 0 16 16"><rect x="1.5" y="3.5" width="13" height="9" fill="none" stroke="#fff" stroke-width="1.4"/><path d="M1.5 3.5L8 9l6.5-5.5" fill="none" stroke="#fff" stroke-width="1.4"/></svg>
        <span>drholcombe@fernwoodchiro-example.com</span>
      </li>
      <li>
        <svg viewBox="0 0 16 16"><circle cx="8" cy="8" r="6.3" fill="none" stroke="#fff" stroke-width="1.3"/><path d="M1.7 8h12.6M8 1.7c-3 3.5-3 9.1 0 12.6M8 1.7c3 3.5 3 9.1 0 12.6" fill="none" stroke="#fff" stroke-width="1.1"/></svg>
        <span>www.fernwoodchiro-example.com</span>
      </li>
    </ul>
  </div>
</body>
</html>
```